Unique Builder wordpress website - Supply Graphics Only

We need a brand new website for a building company in Perth, Australia who constructs insulated panels (sip).
What is a SIP?
A SIP is a high-performance building panel used for floors, walls, and roofs in residential and commercial buildings. Panels are typically made using Expanded Polystyrene (EPS) sandwiched between two structural skins.
The design must incorporate a slick professional look and keep to the logo colours (Lime green & Blacks). The logo must not change colours or be altered. (
We will convert the graphics to a wordpress site. We have our own coders)
Design:
The website design must be clean, mobile friendly and the final design will be adapted to WordPress CMS.
The menus must contain dropdown menus and front page may contain a youtube video at a later date.
Fonts must be clear and easy to read
The contact us page will need to have an online form and google map.
The 16 pages listed will be the complete site and are for reference only. For this project the winning designer would need to supply the Homepage, and 1 inner pages only as PSD files.
The structure is as follows:
Home
About us
High Tech Homes
What is a sip
Benefits
FAQ
Designs
Residential
Granny Flats
Architectural design
Photo Gallery <--- Would be great if a sample design can be provided
Services
Project management and custom design
Site Assembly
Kit Supply
Contact us
***We don't need the designer to design every page however a 1 inner page would be ideal****
Our Competitors websites
Note: the following websites look crap however, the following websites are some of our competitors. We want a clean and awesome layout.
http://www.vorkalite.com.au/
http://trenmoreworks.com.au/
http://www.bralvexa.net.au/
New home builders and commercial builders
Building
5+ page

```html
<!DOCTYPE html>
<html lang="en">
<head>
<meta charset="utf-8">
<title>Kerrowan Build — Advanced Building Technology</title>
<link rel="stylesheet" href="https://fonts.googleapis.com/css2?family=Oswald:wght@400;500&family=Lato:wght@400;700&family=Rubik:wght@400&display=swap">
<style>
:root{
  --lime:#9cc832;
  --lime-soft:#d5e8a2;
  --ink:#2f2f2f;
  --dark:#333333;
  --darker:#2a2a2a;
  --contact-bg:#3b3b3b;
  --panel:#f1f1f1;
  --text:#555555;
  --rule:#d8d8d8;
  --white:#ffffff;
}
*{margin:0;padding:0;box-sizing:border-box}
html,body{width:1200px;height:2250px;overflow:hidden}
body{position:relative;background:var(--white);font-family:'Lato',sans-serif;color:var(--text)}
.abs{position:absolute}
.top-rule{left:0;top:0;width:1200px;height:3px;background:var(--lime)}

/* header */
.brand{left:99px;top:28px;display:flex;align-items:center;gap:14px}
.brand-mark{width:30px;height:30px;background:var(--lime)}
.brand-name{font-family:'Oswald',sans-serif;font-weight:500;font-size:40px;color:var(--lime);line-height:1}
.contact-chip{top:34px;display:flex;align-items:center;gap:18px;font-family:'Oswald',sans-serif;font-weight:400;font-size:18px;color:var(--ink)}
.chip-icon{width:52px;height:40px}

/* nav */
.main-nav{left:0;top:105px;width:1200px;height:35px;background:var(--dark)}
.main-nav ul{list-style:none;display:flex;position:absolute;left:99px;top:0;height:35px}
.main-nav li{font-family:'Oswald',sans-serif;font-weight:400;font-size:16px;color:var(--white);height:35px;line-height:35px;padding:0 24px;border-right:1px solid #4a4a4a}
.main-nav li.is-active{background:var(--lime)}

/* hero */
.hero{left:0;top:140px;width:1200px;height:426px;background:linear-gradient(180deg,#5b5f7a 0%,#8a7a88 35%,#b6866a 55%,#5a5a3c 75%,#2f3826 100%)}
.hero-caption{left:0;top:474px;width:1200px;text-align:center;font-family:'Rubik',sans-serif;font-weight:400;font-size:23px;line-height:35px;color:var(--white);text-shadow:0 1px 3px rgba(0,0,0,.6)}
.hero-arrow{top:325px;width:30px;height:50px}

/* section titles */
.section-title{font-family:'Oswald',sans-serif;font-weight:400;font-size:30px;color:var(--ink);text-align:center;width:1200px;left:0}
.section-title em{font-style:normal;color:var(--lime)}
.title-rule{left:380px;width:440px;height:1px;background:var(--rule)}

/* about */
.about-heading{left:99px;top:606px;display:flex;align-items:center;gap:14px;font-family:'Oswald',sans-serif;font-weight:400;font-size:21px;color:var(--ink)}
.about-heading-mark{width:14px;height:14px;background:var(--lime);flex:none}
.about-heading em{font-style:normal;color:var(--lime);font-size:28px}
.about-heading-rule{left:99px;top:644px;width:658px;height:1px;background:var(--rule)}
.about-copy{left:99px;top:664px;width:660px;font-size:14px;line-height:23px;color:var(--text)}
.read-more{left:99px;top:778px;width:92px;height:34px;background:var(--lime);font-family:'Oswald',sans-serif;font-weight:400;font-size:14px;color:var(--ink);line-height:34px;padding-left:12px}
.video{left:815px;top:609px;width:285px;height:186px;background:linear-gradient(160deg,#4e4e4e,#8a8a86 50%,#5a5a5a);box-shadow:0 6px 10px rgba(0,0,0,.25)}
.video-bar{left:815px;top:775px;width:285px;height:20px;background:#1e1e1e}
.video-track{left:850px;top:783px;width:135px;height:4px;background:#6a7fb0;border-radius:2px}
.video-play{left:822px;top:779px;width:12px;height:12px;background:#2b5fb8}

/* benefits */
.benefits{left:0;top:848px;width:1200px;height:510px;background:var(--panel)}
.benefit h3{font-family:'Oswald',sans-serif;font-weight:400;font-size:19px;color:var(--ink);margin-bottom:8px}
.benefit p{font-size:13px;line-height:18px;color:var(--text)}
.benefit .more{color:var(--lime)}
.benefit.left{text-align:right;width:300px}
.benefit.right{text-align:left;width:300px}

/* projects */
.project-card{top:1479px;width:195px;height:241px;border:2px solid var(--lime-soft);background:var(--white);text-align:center}
.project-photo{position:absolute;left:4px;top:4px;width:183px;height:125px}
.project-card h4{position:absolute;left:0;top:141px;width:100%;font-family:'Oswald',sans-serif;font-weight:400;font-size:16px;color:var(--ink)}
.project-card p{position:absolute;left:10px;top:171px;width:171px;font-size:12px;line-height:16px;color:var(--text)}
.project-plus{position:absolute;left:70px;top:220px;width:56px;height:42px}
.ph-1{background:linear-gradient(180deg,#a9c4e0,#b48d63 60%,#4d4a44)}
.ph-2{background:linear-gradient(180deg,#c98b4e,#e2b27a 50%,#7c5a3c)}
.ph-3{background:linear-gradient(180deg,#d0d6d2,#b99c76 55%,#5b6a4a)}
.ph-4{background:linear-gradient(180deg,#1f3f93,#3a5fb8 55%,#1b2340)}
.proj-arrow{top:1568px;width:36px;height:64px}

/* contact */
.contact{left:0;top:1775px;width:1200px;height:430px;background:var(--contact-bg)}
.contact .section-title{color:var(--white)}
.field{left:99px;width:291px;height:37px;background:var(--white);border-radius:3px;font-size:12px;color:#555;padding:11px 10px}
.submit{left:99px;top:2136px;width:94px;height:34px;background:var(--lime-soft);border-radius:3px;font-family:'Oswald',sans-serif;font-weight:400;font-size:15px;color:var(--ink);text-align:center;line-height:34px}
.map{left:451px;top:1910px;width:351px;height:208px;background:linear-gradient(135deg,#b9d3ee,#e9e4d0 45%,#c6dca8 70%,#a8c6e6)}
.info-row{left:867px;width:235px;display:flex;gap:16px;font-size:13px;color:var(--white);line-height:17px}
.info-row strong{font-weight:700}
.info-rule{left:867px;width:235px;height:1px;background:#4d4d4d}
.info-icon{width:14px;height:14px;flex:none;margin-top:2px}

/* footer */
.site-footer{left:0;top:2205px;width:1200px;height:45px;background:var(--lime)}
.copyright{left:99px;top:2220px;font-size:11px;font-weight:700;color:var(--ink)}
.social{top:2216px;width:22px;height:22px;background:var(--dark)}
</style>
</head>
<body>

<div class="abs top-rule"></div>

<header>
  <div class="abs brand">
    <span class="brand-mark"></span>
    <span class="brand-name">Kerrowan Build</span>
  </div>
  <div class="abs contact-chip" style="left:705px">
    <svg class="chip-icon" viewBox="0 0 52 40"><polygon points="0,20 13,0 39,0 52,20 39,40 13,40" fill="var(--lime-soft)"/><path d="M20 12c2-1 3 0 4 3l-2 2c1 3 3 5 6 6l2-2c3 1 4 2 3 4-1 2-3 3-6 2-6-2-10-6-11-11 0-2 1-3 4-4z" fill="var(--ink)"/></svg>
    <span>987-654-3210</span>
  </div>
  <div class="abs contact-chip" style="left:893px">
    <svg class="chip-icon" viewBox="0 0 52 40"><polygon points="0,20 13,0 39,0 52,20 39,40 13,40" fill="var(--lime-soft)"/><rect x="16" y="13" width="20" height="14" fill="var(--ink)"/><path d="M16 13l10 8 10-8" stroke="var(--lime-soft)" stroke-width="1.5" fill="none"/></svg>
    <span>info@kerrowanbuild.com</span>
  </div>
</header>

<nav class="abs main-nav">
  <ul>
    <li class="is-active">Home</li>
    <li>About Us</li>
    <li>High Tech Homes</li>
    <li>What is a sip</li>
    <li>Benefits</li>
    <li>FAQs</li>
    <li>Designs</li>
    <li>Services</li>
    <li>Contact Us</li>
  </ul>
</nav>

<section>
  <div class="abs hero" role="img" aria-label="Photograph of a modern timber and glass home at sunset with a family walking on the lawn"></div>
  <svg class="abs hero-arrow" style="left:52px" viewBox="0 0 30 50"><path d="M24 4L6 25l18 21" stroke="#fff" stroke-width="2" fill="none"/></svg>
  <svg class="abs hero-arrow" style="left:1118px" viewBox="0 0 30 50"><path d="M6 4l18 21L6 46" stroke="#fff" stroke-width="2" fill="none"/></svg>
  <p class="abs hero-caption">We Specialize In Supplying On Time And On Budget, With High Quality Structural Kits<br>To Builders And Developers Specific To Their Needs Or Requirements</p>
</section>

<section>
  <h2 class="abs about-heading">
    <span class="about-heading-mark"></span>
    <span>ABOUT <em>Kerrowan Build</em> ADVANCED BUILDING TECHNOLOGY</span>
  </h2>
  <div class="abs about-heading-rule"></div>
  <p class="abs about-copy">Lorem ipsum dolor sit amet, consectetuer adipiscing elit, sed diam nonummy nibh euismod tincidunt ut laoreet dolore magna aliquam erat volutpat. Ut wisi enim ad minim veniam, quis nostrud exerci tation ullamcorper suscipit lobortis nisl ut aliquip ex ea commodo consequat. Duis autem vel eum iriure dolor in hendrerit in vulputate velit esse molestie consequat...</p>
  <div class="abs read-more">Read More</div>
  <div class="abs video" role="img" aria-label="Video still of workers assembling insulated panels in a factory"></div>
  <div class="abs video-bar"></div>
  <div class="abs video-play"></div>
  <div class="abs video-track"></div>
</section>

<section class="abs benefits">
  <h2 class="abs section-title" style="top:35px">Our <em>Benefits</em></h2>
  <div class="abs title-rule" style="top:82px"></div>

  <div class="abs benefit left" style="left:74px;top:176px">
    <h3>High Level Of Captive Insulation.</h3>
    <p>Ut wisi enim ad minim veniam, quismpi<br><span class="more">[+]</span>....&nbsp; nostrud exerci tation ullamco</p>
  </div>
  <div class="abs benefit left" style="left:74px;top:360px">
    <h3>Reduced Build Time</h3>
    <p>Ut wisi enim ad minim veniam, quismpi<br><span class="more">[+]</span>....&nbsp; nostrud exerci tation ullamco</p>
  </div>
  <div class="abs benefit right" style="left:825px;top:176px">
    <h3>Very Strong, Light Weight And Durable</h3>
    <p>Ut wisi enim ad minim veniam, quismpi<br>nostrud exerci tation ullamco ....<span class="more">[+]</span></p>
  </div>
  <div class="abs benefit right" style="left:825px;top:360px">
    <h3>Energy Efficient</h3>
    <p>Ut wisi enim ad minim veniam, quismpi<br>nostrud exerci tation ullamco ....<span class="more">[+]</span></p>
  </div>

  <svg class="abs" style="left:400px;top:112px" width="400" height="340" viewBox="0 0 400 340">
    <polygon points="150,60 250,60 262,112 138,112" fill="#8a8a8a"/>
    <polygon points="150,230 250,230 262,284 138,284" fill="#8a8a8a"/>
    <g fill="var(--dark)" stroke="var(--lime-soft)" stroke-width="4">
      <polygon points="11,78 51,18 129,18 169,78 129,138 51,138"/>
      <polygon points="229,78 269,18 347,18 387,78 347,138 269,138"/>
      <polygon points="11,267 51,207 129,207 169,267 129,327 51,327"/>
      <polygon points="229,267 269,207 347,207 387,267 347,327 269,327"/>
      <polygon points="50,172 110,105 290,105 350,172 290,240 110,240"/>
    </g>
    <g stroke="#fff" stroke-width="3" fill="none">
      <rect x="68" y="60" width="44" height="32" rx="2"/>
      <circle cx="92" cy="92" r="8"/>
      <rect x="292" y="66" width="22" height="14" rx="7" transform="rotate(-45 303 73)"/>
      <rect x="302" y="76" width="22" height="14" rx="7" transform="rotate(-45 313 83)"/>
      <path d="M104 267a14 14 0 1 1-4-10"/>
      <path d="M90 259v9l6 4"/>
    </g>
    <polygon points="312,244 298,270 308,270 302,292 320,262 310,262 318,244" fill="#fff"/>
    <text x="200" y="158" text-anchor="middle" font-family="Oswald, sans-serif" font-size="22" fill="var(--lime)">20 + Year</text>
    <text x="200" y="183" text-anchor="middle" font-family="Oswald, sans-serif" font-size="15" fill="#fff">History Of Performance In</text>
    <text x="200" y="205" text-anchor="middle" font-family="Oswald, sans-serif" font-size="15" fill="#fff">Cyclonic Locations In WA</text>
  </svg>
</section>

<section>
  <h2 class="abs section-title" style="top:1390px">Recent <em>Projects</em></h2>
  <div class="abs title-rule" style="top:1440px"></div>
  <svg class="abs proj-arrow" style="left:63px" viewBox="0 0 36 64"><path d="M32 2L4 32l28 30" stroke="#aaa" stroke-width="1.5" fill="none"/></svg>
  <svg class="abs proj-arrow" style="left:1101px" viewBox="0 0 36 64"><path d="M4 2l28 30L4 62" stroke="#aaa" stroke-width="1.5" fill="none"/></svg>

  <article class="abs project-card" style="left:135px">
    <div class="project-photo ph-1" role="img" aria-label="Photograph of a long timber-clad commercial building"></div>
    <h4>Lorem Ipsum Sit Dolor</h4>
    <p>Lorem ipsum dolor sit amet, consectetuer adipisc</p>
    <svg class="project-plus" viewBox="0 0 56 42"><polygon points="0,21 14,0 42,0 56,21 42,42 14,42" fill="var(--lime)"/><path d="M28 15v12M22 21h12" stroke="var(--ink)" stroke-width="2.5"/></svg>
  </article>
  <article class="abs project-card" style="left:380px">
    <div class="project-photo ph-2" role="img" aria-label="Photograph of a timber-lined library interior"></div>
    <h4>Lorem Ipsum Sit Dolor</h4>
    <p>Lorem ipsum dolor sit amet, consectetuer adipisc</p>
    <svg class="project-plus" viewBox="0 0 56 42"><polygon points="0,21 14,0 42,0 56,21 42,42 14,42" fill="var(--lime)"/><path d="M28 15v12M22 21h12" stroke="var(--ink)" stroke-width="2.5"/></svg>
  </article>
  <article class="abs project-card" style="left:622px">
    <div class="project-photo ph-3" role="img" aria-label="Photograph of a timber-clad house among trees"></div>
    <h4>Lorem Ipsum Sit Dolor</h4>
    <p>Lorem ipsum dolor sit amet, consectetuer adipisc</p>
    <svg class="project-plus" viewBox="0 0 56 42"><polygon points="0,21 14,0 42,0 56,21 42,42 14,42" fill="var(--lime)"/><path d="M28 15v12M22 21h12" stroke="var(--ink)" stroke-width="2.5"/></svg>
  </article>
  <article class="abs project-card" style="left:867px">
    <div class="project-photo ph-4" role="img" aria-label="Photograph of a lit building at dusk"></div>
    <h4>Lorem Ipsum Sit Dolor</h4>
    <p>Lorem ipsum dolor sit amet, consectetuer adipisc</p>
    <svg class="project-plus" viewBox="0 0 56 42"><polygon points="0,21 14,0 42,0 56,21 42,42 14,42" fill="var(--lime)"/><path d="M28 15v12M22 21h12" stroke="var(--ink)" stroke-width="2.5"/></svg>
  </article>
</section>

<section class="abs contact">
  <h2 class="abs section-title" style="top:28px">Contact <em>Us</em></h2>
  <div class="abs title-rule" style="top:78px;background:#555"></div>
</section>
<div class="abs field" style="top:1906px">Your Name</div>
<div class="abs field" style="top:1954px">Your Email Address</div>
<div class="abs field" style="top:2002px">Your Phone Number</div>
<div class="abs field" style="top:2050px;height:73px">Your Message</div>
<div class="abs submit">SUBMIT</div>
<div class="abs map" role="img" aria-label="Street map showing the office location with a pin"></div>

<div class="abs info-row" style="top:1906px">
  <svg class="info-icon" viewBox="0 0 14 14"><path d="M7 0a5 5 0 0 1 5 5c0 4-5 9-5 9S2 9 2 5a5 5 0 0 1 5-5z" fill="var(--lime)"/><circle cx="7" cy="5" r="2" fill="var(--contact-bg)"/></svg>
  <div><strong>Kerrowan Build</strong><br>123 euismod cidun ut laoreetmok laoreet dol magnak aliquam&nbsp; sit PG Feugait.</div>
</div>
<div class="abs info-rule" style="top:1990px"></div>
<div class="abs info-row" style="top:2005px">
  <svg class="info-icon" viewBox="0 0 14 14"><path d="M3 1c1.5-.7 2.3 0 3 2L5 4.5c.7 2 2 3.3 4 4L10.5 7c2 .7 2.7 1.5 2 3-.7 1.7-2.3 2.3-4.5 1.5C4.5 10 3 8.5 1.5 4.5 1 3 1.5 1.7 3 1z" fill="var(--lime)"/></svg>
  <div>(987) 654 - 3210</div>
</div>
<div class="abs info-rule" style="top:2040px"></div>
<div class="abs info-row" style="top:2055px">
  <svg class="info-icon" viewBox="0 0 14 14"><rect x="3" y="1" width="8" height="4" fill="var(--lime)"/><rect x="1" y="5" width="12" height="5" fill="var(--lime)"/><rect x="3" y="9" width="8" height="4" fill="var(--lime)" stroke="var(--contact-bg)"/></svg>
  <div>(987) 654 - 3210</div>
</div>
<div class="abs info-rule" style="top:2090px"></div>
<div class="abs info-row" style="top:2105px">
  <svg class="info-icon" viewBox="0 0 14 14"><rect x="1" y="3" width="12" height="8" fill="var(--lime)"/><path d="M1 3l6 5 6-5" stroke="var(--contact-bg)" stroke-width="1.2" fill="none"/></svg>
  <div>info@KerrowanBuild.com</div>
</div>

<footer>
  <div class="abs site-footer"></div>
  <p class="abs copyright">© 2016 Kerrowan Build ADVANCED BUILDING TECHNOLOGY. All Right Reserved.</p>
  <span class="abs social" style="left:983px"></span>
  <span class="abs social" style="left:1016px"></span>
  <span class="abs social" style="left:1048px"></span>
  <span class="abs social" style="left:1080px"></span>
</footer>

</body>
</html>
```